Skin care manufacturer looking for packaging design for new skin care brand.

We need a design and logo for a skin care brand to be sold at retail stores and online in the United States and Europe. The design will be for 1.7oz - 2oz serums that will not have a retail box. The name of the brand is Orvia Lune and should be a luxurious brand that is approachable. The brand will consist of 4 face serums - Vitamin C, Collagen, Retinol and Hyaluronic Acid that all contain Dead Sea Minerals. Images shown are for inspiration only. Color of bottles can be varied based on design and bottles can be screen printed or labeled.

```html
<!DOCTYPE html>
<html lang="en">
<head>
<meta charset="utf-8">
<title>Orvia Lune — Face Serum Labels</title>
<link rel="stylesheet" href="https://fonts.googleapis.com/css2?family=Josefin+Sans:wght@300&family=Jost:wght@300&family=Montserrat:wght@400;500&display=swap">
<style>
  :root {
    --bg: #2c303b;
    --ink: #111318;
    --line: #5d5f6b;
    --lilac-top: #d2d0fb;
    --lilac-mid: #efedfd;
    --lilac-band: #b8b6f4;
    --pink-top: #e9b3de;
    --pink-mid: #f7e3f2;
    --pink-band: #dc9bd2;
    --white: #ffffff;
  }
  * { box-sizing: border-box; margin: 0; padding: 0; }
  html, body { width: 1200px; height: 971px; overflow: hidden; }
  body { background: var(--bg); position: relative; font-family: "Montserrat", sans-serif; }

  .label {
    position: absolute;
    top: 175px;
    width: 460px;
    height: 620px;
    overflow: hidden;
  }
  .label--vitamin-c {
    left: 100px;
    background: linear-gradient(160deg, var(--lilac-top) 0%, var(--lilac-mid) 45%, var(--lilac-top) 100%);
    --band: var(--lilac-band);
    --sprig: #b9b7e6;
  }
  .label--collagen {
    left: 640px;
    background: linear-gradient(160deg, var(--pink-top) 0%, var(--pink-mid) 45%, var(--pink-top) 100%);
    --band: var(--pink-band);
    --sprig: #d39fcb;
  }

  .sprig {
    position: absolute;
    border-radius: 50%;
    background: radial-gradient(ellipse at center, var(--sprig) 0%, transparent 70%);
    opacity: .8;
  }
  .sprig--top { left: 20px; top: 0; width: 260px; height: 150px; }
  .sprig--bottom { right: -10px; bottom: -10px; width: 260px; height: 150px; }

  .brand {
    position: absolute;
    top: 158px;
    width: 100%;
    text-align: center;
    font-family: "Josefin Sans", sans-serif;
    font-weight: 300;
    font-size: 42px;
    letter-spacing: 3px;
    color: var(--ink);
  }

  .product-band {
    position: absolute;
    top: 240px;
    width: 100%;
    height: 132px;
    background: var(--band);
    text-align: center;
  }
  .product-name {
    font-family: "Jost", sans-serif;
    font-weight: 300;
    font-size: 66px;
    line-height: 1;
    letter-spacing: -1.5px;
    color: var(--white);
    padding-top: 16px;
  }
  .product-type {
    font-family: "Josefin Sans", sans-serif;
    font-weight: 300;
    font-size: 27px;
    letter-spacing: 9px;
    color: var(--ink);
    margin-top: 6px;
  }

  .benefits {
    position: absolute;
    top: 398px;
    width: 100%;
    list-style: none;
    text-align: center;
    font-size: 14px;
    font-weight: 500;
    line-height: 25px;
    color: var(--ink);
  }

  .size {
    position: absolute;
    left: 60px;
    bottom: 58px;
    font-size: 14px;
    color: var(--ink);
  }
</style>
</head>
<body>
  <section class="label label--vitamin-c">
    <div class="sprig sprig--top" role="img" aria-label="Line-drawn botanical sprig"></div>
    <h1 class="brand">ORVIA LUNE</h1>
    <div class="product-band">
      <p class="product-name">Vitamin C</p>
      <p class="product-type">FACE SERUMS</p>
    </div>
    <ul class="benefits">
      <li>BOOSTS COLLAGEN</li>
      <li>BRIGHTENS COMPLEXION</li>
      <li>PROTECTS FROM SUN DAMAGE</li>
      <li>REDUCES HYPERPIGMENTATION</li>
    </ul>
    <p class="size">2OZ / 60 ML</p>
    <div class="sprig sprig--bottom" role="img" aria-label="Line-drawn flowering branch"></div>
  </section>

  <section class="label label--collagen">
    <div class="sprig sprig--top" role="img" aria-label="Line-drawn botanical sprig"></div>
    <h2 class="brand">ORVIA LUNE</h2>
    <div class="product-band">
      <p class="product-name">Collagen</p>
      <p class="product-type">FACE SERUMS</p>
    </div>
    <ul class="benefits">
      <li>ANTI AGING</li>
      <li>ANTI WRINKLES</li>
      <li>IMPROVES SKIN TEXTURE</li>
    </ul>
    <p class="size">2OZ / 60 ML</p>
    <div class="sprig sprig--bottom" role="img" aria-label="Line-drawn flowering branch"></div>
  </section>
</body>
</html>
```